Emergency Management Consulting Needs a Website

Need to develop a website for an Emergency Management Consulting business. This website needs to be user friendly and resemble disaster preparedness, response, recovery, and mitigation. It must allow for me to make changes to it myself by adding pages, content and pictures. Looking for an advanced page to the website that allows monitoring of social media sites, hashtags, and keywords. Must have pictures of disasters on the site. Must try to integrate the logo colors, not excessive.

Reason: Did not receive anything sufficient to what I am looking for.

Industry/Entity Type

Government

Coding

Coded - Design and coding required

Number of Pages Required

5+ page

Requirements
Must have
• Logo, advanced social media monitoring page, allow for edits myself (content, pages, graphics) this must be a CMS of some sort, use logo color scheme (not excessively), must be professional looking, connect with Vexlo Domain, find a hosting site, SEO, no "long" designs, minimize "dead" space, no social media feeds, no newsletter stuff.
• Menu items: Home, About Us, Services, Situation Monitor, Work With Us, Contact Us (hopefully these could be editable if I need to later)
• When you make a submission, please send me a message on which CMS you are using. Thank you.
Nice to have
• Examples of websites:
• https://www.plorn.vic.gov.au/
• http://www.garvelmunds.com/
• http://www.tqplaxr.org/
• http://dumbrellconsulting.com/
• http://www.folvantix.com/services/emergency-management
• https://qzu.com/
• http://www.belmorvia.com/Responsibility/Sustainable-Development/HSE/Crisis-and-Emergency-Management/

```html
<!DOCTYPE html>
<html lang="en">
<head>
<meta charset="utf-8">
<title>Stonebrook Emergency Management</title>
<link href="https://fonts.googleapis.com/css2?family=Source+Sans+3:ital,wght@0,300;0,400;0,600;0,700;1,300;1,400&display=swap" rel="stylesheet">
<style>
:root{
  --orange:#f5a012;
  --orange-deep:#ef8a0c;
  --ink:#2b2b2b;
  --muted:#7a7a7a;
  --white:#ffffff;
  --sky:#2a8fd8;
}
*{margin:0;padding:0;box-sizing:border-box}
html,body{width:1200px;height:2500px;overflow:hidden}
body{position:relative;background:var(--white);font-family:"Source Sans 3",sans-serif;color:var(--ink)}
.abs{position:absolute}
.btn{position:absolute;display:flex;align-items:center;justify-content:center;background:linear-gradient(var(--orange),var(--orange-deep));color:var(--white);font-size:13px;text-transform:uppercase;letter-spacing:.3px}

/* hero */
.hero{left:0;top:0;width:1200px;height:537px;
  background:
    radial-gradient(ellipse 420px 260px at 80% 25%,rgba(190,200,210,.45),transparent 70%),
    radial-gradient(ellipse 380px 220px at 25% 70%,rgba(160,120,85,.55),transparent 70%),
    radial-gradient(ellipse 300px 200px at 70% 80%,rgba(110,110,130,.45),transparent 70%),
    linear-gradient(180deg,#7a6a58 0%,#6b5341 45%,#4e3a2a 100%)}
.hero-shade{left:0;top:0;width:1200px;height:537px;background:rgba(0,0,0,.18)}
.topbar{left:0;top:0;width:1200px;height:78px;background:rgba(20,20,20,.85)}
.brand{left:155px;top:22px;display:flex;align-items:center;gap:10px;color:var(--white);font-weight:700;font-size:24px;letter-spacing:.5px}
.brand-dot{width:34px;height:34px;border-radius:50%;background:var(--orange)}
.nav{left:513px;top:0;height:78px;font-size:14px;text-transform:uppercase}
.nav a{position:absolute;top:36px;color:var(--white);text-decoration:none;white-space:nowrap}
.nav a.active{color:var(--orange)}
.nav-mark{left:498px;top:0;width:88px;height:4px;background:var(--orange)}
.phone{left:915px;top:33px;display:flex;align-items:center;gap:8px;color:var(--white);font-size:17px}
.hero-title{left:0;width:1200px;top:256px;text-align:center;color:var(--white);font-size:27px;font-weight:300;line-height:32px}
.hero-title b{font-weight:400;font-size:23px}
.dots{left:575px;top:502px;display:flex;gap:7px}
.dots i{width:6px;height:6px;border-radius:50%;background:rgba(255,255,255,.55)}
.dots i.on{background:var(--white)}

/* about */
.eyebrow{font-size:12.5px;letter-spacing:.4px;text-transform:uppercase;color:#444}
.rule{height:2px;width:53px;background:var(--orange)}
.about-head{left:232px;top:634px;width:340px;font-size:23px;line-height:29px;color:#333;font-weight:400}
.about-copy{left:232px;top:766px;width:350px;font-size:12.5px;line-height:19px;color:var(--muted)}
.about-photo{left:688px;top:600px;width:280px;height:320px;
  background:
    radial-gradient(ellipse 110px 160px at 12% 25%,rgba(40,70,40,.75),transparent 70%),
    radial-gradient(ellipse 140px 200px at 75% 40%,rgba(170,140,100,.8),transparent 70%),
    linear-gradient(180deg,#e4e6e4 0%,#c9c7bf 35%,#8f8371 70%,#7a4f3c 100%)}

/* team */
.team{left:0;top:983px;width:1200px;height:400px;
  background:
    radial-gradient(ellipse 500px 220px at 50% 50%,rgba(90,88,84,.5),transparent 70%),
    linear-gradient(90deg,#2a2927 0%,#3b3936 30%,#34322f 70%,#262523 100%)}
.team-word{left:0;width:1200px;top:990px;text-align:center;font-size:135px;line-height:150px;font-weight:700;color:rgba(255,255,255,.16);letter-spacing:4px}
.avatar{border-radius:50%;background:linear-gradient(#b9a898,#7d6e62)}
.quote{left:0;width:1200px;top:1144px;text-align:center;color:#f0f0f0;font-style:italic;font-size:18.5px;line-height:23px;font-weight:300}
.person{left:0;width:1200px;top:1236px;text-align:center;color:var(--white);font-size:17px}
.person small{display:block;font-size:12px;margin-top:-2px}

/* cases */
.cases-head{left:232px;top:1482px;font-size:22px;color:#333;font-weight:400}
.card{overflow:hidden}
.card-label{position:absolute;left:15px;bottom:18px;color:var(--white);font-size:17px;font-weight:300;line-height:19px}
.card-label small{display:block;font-size:10.5px;font-weight:600}
.read-more{position:absolute;left:15px;color:var(--orange);font-size:11px;font-weight:600}

/* footer */
.foot-left{left:0;top:2028px;width:600px;height:472px;background:radial-gradient(ellipse 300px 160px at 40% 80%,rgba(70,66,60,.6),transparent 70%),linear-gradient(180deg,#262523,#1c1b1a)}
.foot-right{left:600px;top:2028px;width:600px;height:472px;background:radial-gradient(ellipse 300px 180px at 60% 75%,rgba(90,86,80,.5),transparent 70%),linear-gradient(180deg,#403f3d,#2b2927)}
.foot-title{color:var(--white);font-size:18px}
.foot-text{color:#d6d6d6;font-size:12.5px;line-height:16px}
.foot-strong{color:var(--white);font-size:17px}
.field{left:688px;width:280px;border-bottom:1px solid #8a8a8a;color:#cfcfcf;font-size:12.5px;padding:0 0 6px 6px}
.social{left:230px;top:2346px;display:flex;gap:8px}
.social i{width:24px;height:24px;border-radius:50%}
</style>
</head>
<body>

<!-- hero -->
<div class="abs hero" role="img" aria-label="Photo of rescue workers in helmets searching through the rubble of collapsed houses"></div>
<div class="abs hero-shade"></div>
<div class="abs topbar"></div>
<div class="abs brand"><span class="brand-dot"></span>STONEBROOK</div>
<div class="abs nav-mark"></div>
<nav class="abs nav">
  <a class="active" style="left:0">About Us</a>
  <a style="left:99px">Services</a>
  <a style="left:190px">Team</a>
  <a style="left:255px">Contact Us</a>
</nav>
<div class="abs phone" style="left:935px">
  <svg width="16" height="16" viewBox="0 0 24 24"><path d="M6.6 10.8a15 15 0 0 0 6.6 6.6l2.2-2.2a1 1 0 0 1 1-.25 11 11 0 0 0 3.6.6 1 1 0 0 1 1 1V20a1 1 0 0 1-1 1A17 17 0 0 1 3 4a1 1 0 0 1 1-1h3.5a1 1 0 0 1 1 1 11 11 0 0 0 .6 3.6 1 1 0 0 1-.25 1z" fill="none" stroke="#f5a012" stroke-width="2"/></svg>
  555-014-2290
</div>
<svg class="abs" style="left:52px;top:292px" width="24" height="30" viewBox="0 0 24 30"><path d="M2 2v26M22 15H4m6-6-6 6 6 6" fill="none" stroke="#fff" stroke-opacity=".7" stroke-width="1.5"/></svg>
<svg class="abs" style="left:1120px;top:292px" width="24" height="30" viewBox="0 0 24 30"><path d="M22 2v26M2 15h18m-6-6 6 6-6 6" fill="none" stroke="#fff" stroke-opacity=".7" stroke-width="1.5"/></svg>
<div class="abs hero-title">Recovering from a Disaster is never easy,<br><b>but we will make it easier.</b></div>
<div class="btn" style="left:540px;top:337px;width:120px;height:31px">Contact Us</div>
<svg class="abs" style="left:592px;top:462px" width="16" height="10" viewBox="0 0 16 10"><path d="M1 1l7 7 7-7" fill="none" stroke="#fff" stroke-width="1.5"/></svg>
<div class="abs dots"><i></i><i class="on"></i><i></i><i></i></div>

<!-- about -->
<div class="abs rule" style="left:155px;top:603px"></div>
<div class="abs eyebrow" style="left:232px;top:596px">Stonebrook Emergency Management</div>
<h2 class="abs about-head">A successful disaster recovery program is implemented quickly and accurately, with strong customer service</h2>
<p class="abs about-copy">30+ years of experience in disaster management and a track record of delivering results to help states and cities implement model disaster recovery and resilience programs. We provide results ...</p>
<div class="btn" style="left:232px;top:888px;width:103px;height:30px">About Us</div>
<div class="abs about-photo" role="img" aria-label="Photo of a damaged apartment building with debris and fallen power lines in the street"></div>

<!-- team -->
<div class="abs team" role="img" aria-label="Dark photo of storm-damaged trees and wreckage"></div>
<div class="abs team-word">TEAM</div>
<div class="abs avatar" style="left:480px;top:1062px;width:50px;height:50px;opacity:.85" role="img" aria-label="Team member portrait"></div>
<div class="abs avatar" style="left:562px;top:1049px;width:76px;height:76px;border:3px solid #fff" role="img" aria-label="Portrait of the director"></div>
<div class="abs avatar" style="left:668px;top:1062px;width:50px;height:50px;opacity:.85" role="img" aria-label="Team member portrait"></div>
<svg class="abs" style="left:176px;top:1165px" width="12" height="20" viewBox="0 0 12 20"><path d="M10 2 2 10l8 8" fill="none" stroke="#fff" stroke-width="1.5"/></svg>
<svg class="abs" style="left:1012px;top:1165px" width="12" height="20" viewBox="0 0 12 20"><path d="M2 2l8 8-8 8" fill="none" stroke="#f5a012" stroke-width="1.5"/></svg>
<p class="abs quote">I like the challenge of being able to recommend changes in policies and programs,<br>and to provide commentary and advice to our clients at the highest levels of government.<br>They know Dumbrell is a trusted agent.</p>
<div class="abs person">- DANA RUELLE -<small>Director</small></div>
<div class="btn" style="left:540px;top:1295px;width:120px;height:32px;font-size:12px">Consult Now</div>

<!-- case studies -->
<div class="abs rule" style="left:155px;top:1452px"></div>
<div class="abs eyebrow" style="left:232px;top:1445px">Case Studies</div>
<h2 class="abs cases-head">We’ve helped thousands across the United States.</h2>

<div class="abs card" style="left:233px;top:1538px;width:204px;height:360px;background:radial-gradient(ellipse 90px 70px at 50% 45%,rgba(200,80,40,.55),transparent 70%),linear-gradient(180deg,#6b7a5a 0%,#7d705e 28%,#3f5a78 55%,#2f4560 100%)" role="img" aria-label="Photo of rescue workers wading through floodwater">
  <div class="card-label">Wilmington, NC<small>Active Shooter Scenario</small></div>
</div>
<div class="abs card" style="left:460px;top:1538px;width:278px;height:169px;background:radial-gradient(ellipse 120px 80px at 25% 40%,rgba(160,90,60,.6),transparent 70%),linear-gradient(160deg,#6c7180 0%,#7a5a44 50%,#3e322a 100%)" role="img" aria-label="Photo of a collapsed brick building">
  <div class="card-label" style="bottom:40px">University Park, PA<small>HSEEP-Compliant Functional Exercise</small></div>
  <div class="read-more" style="bottom:14px">+ READ MORE</div>
</div>
<div class="abs card" style="left:460px;top:1730px;width:278px;height:168px;background:radial-gradient(ellipse 120px 60px at 55% 70%,rgba(90,110,140,.55),transparent 70%),linear-gradient(180deg,#9a9ea2 0%,#5e6062 50%,#36383a 100%)" role="img" aria-label="Photo of houses destroyed by a hurricane">
  <div class="card-label">New Orleans, LA<small>Post-Katrina Accounting Support</small></div>
</div>
<div class="abs card" style="left:763px;top:1538px;width:205px;height:360px;background:radial-gradient(ellipse 70px 160px at 80% 35%,rgba(190,130,80,.6),transparent 70%),linear-gradient(180deg,#5a6068 0%,#8a6a4e 40%,#6e5240 75%,#4e3c30 100%)" role="img" aria-label="Photo of a worker in a hard hat clearing storm debris">
  <div class="card-label">New York, NY<small>Hurricane Sandy Recovery</small></div>
</div>
<div class="btn" style="left:233px;top:1932px;width:104px;height:31px;font-size:12px">View All</div>

<!-- footer -->
<div class="abs foot-left" role="img" aria-label="Dark photo of debris under bare trees"></div>
<div class="abs foot-right" role="img" aria-label="Dark photo of a wrecked neighbourhood under a stormy sky"></div>
<div class="abs foot-title" style="left:230px;top:2085px">Contact Us</div>
<div class="abs foot-text" style="left:230px;top:2125px">Need Help? Call Us any time</div>
<div class="abs foot-strong" style="left:230px;top:2144px">555-014-2290</div>
<div class="abs foot-text" style="left:230px;top:2178px">Email:<br>info@stonebrookem.com</div>
<div class="abs foot-text" style="left:230px;top:2223px">Location:<br>720 Alder Bend Rd, Marrowfield,<br>MN, 55990</div>
<div class="abs social">
  <i style="background:#3b5a98"></i><i style="background:#d6402e"></i><i style="background:#2ca0dc"></i><i style="background:#d42a25"></i>
</div>
<div class="abs foot-text" style="left:230px;top:2404px">© 2016 Stonebrook Emergency Management<br>All rights reserved.</div>

<div class="abs foot-title" style="left:688px;top:2085px">Send us Message</div>
<div class="abs field" style="top:2125px">Your Name</div>
<div class="abs field" style="top:2175px">Email</div>
<div class="abs field" style="top:2226px">Phone</div>
<div class="abs field" style="top:2277px;height:93px">Type your Message</div>
<div class="btn" style="left:688px;top:2405px;width:104px;height:30px;gap:6px">
  <svg width="12" height="12" viewBox="0 0 12 12"><path d="M0 5 12 0 8 12 6 7z" fill="#fff"/></svg>Send
</div>
<svg class="abs" style="left:1084px;top:2422px" width="22" height="12" viewBox="0 0 22 12"><path d="M11 0 22 12H0z" fill="#2a8fd8"/></svg>

</body>
</html>
```